Web design for software company

I'm a software developer that designs high end specialist web applications, mobile apps and user friendly applications for medium to large customers. I integrate different systems together within a company and provide web based applications or mobile apps to view and edit information in that web of linked systems.

I currently work alone, basically selling my time on specialist projects, but also build my own software solutions which I eventually want to put into the market.

My company name is Overthread (lowercase 'L' for logic) and I work from the Netherlands. I've attached my current logo which is basically just text in VOXbox font. Current colours are mustard yellow and grey, but i'm open to other options to better fit the web design.

I've got a sort of slogan: "Specialized software development" - better ideas are welcome. The slogan in the logo attachment is older.

I'm looking for a site design that reflects my work as being on the cutting edge of technology, but being clear and simple. My thinking with the name Overthread is that it refers to the underlying mechanism and logic of software.

The site will not be text heavy, so some kind of large graphic to do with software design is welcome. I expect about 4 or 5 main pages or sections of the site in which i'll eventually add things like a blog or contact info etc.

Industry/Entity Type

It Company

Number of Pages Required

1 page

Font styles to use
Sans Serif

Requirements
Nice to have
• A large graphic or photo relevant to my focus as a software developer. Something that shows connecting of software systems with perhaps a variety of devices/browsers that would display data from that cloud of systems.
• Something like these (allthough these are ugly - but the idea is what i mean):
• http://img4.pixvaultimages.example/2000517/22458/i/450/pixvault_224581133-Cloud-computing-user-interface.jpg
• http://business.tamblinet.example/images/modules/mobile-device-policy-design-banner.png
• https://www.pagecraftly.example/images/responsive-web-design.jpg
• http://www.norvexa.example/images/web_apps.png
• https://www.keyportal.example/assets/img/product/web-app@2x.png?v2
Should not have
• Photographs of smiling happy people looking at a screen that make it look like it's a huge business with many offices. I'm a one-man company which could perhaps grow a little bit, but i want to focus on my expertise instead of size.

```html
<!DOCTYPE html>
<html lang="en">
<head>
<meta charset="utf-8">
<title>Overthread — Specialised Software Development</title>
<link href="https://fonts.googleapis.com/css2?family=Open+Sans:ital,wght@0,400;0,600;0,700;0,800;1,400;1,600&family=Raleway:wght@400;500;600&display=swap" rel="stylesheet">
<style>
:root{
  --yellow:#fcd518;
  --yellow-deep:#f2c500;
  --dark:#2b2b2b;
  --darker:#1d1d1d;
  --footer:#272727;
  --ink:#222;
  --navy:#1f2a44;
  --muted:#555;
  --light:#f1f1f1;
  --white:#fff;
}
*{margin:0;padding:0;box-sizing:border-box}
html,body{width:1200px;height:2579px;overflow:hidden}
body{position:relative;font-family:'Open Sans',Arial,sans-serif;color:var(--ink);background:var(--white)}
.abs{position:absolute}
.brand{font-family:'Open Sans',Arial,sans-serif;font-weight:800;color:var(--yellow);letter-spacing:1px;text-transform:uppercase}

/* header */
.site-header{position:absolute;left:0;top:0;width:1200px;height:95px;background:var(--dark)}
.site-header .brand{position:absolute;left:98px;top:26px;font-size:32px;line-height:36px}
.main-nav{position:absolute;right:98px;top:0;display:flex;gap:36px;height:95px}
.main-nav a{color:var(--white);text-decoration:none;font-size:14px;line-height:95px;position:relative;text-transform:uppercase}
.main-nav a.active::after{content:"";position:absolute;left:0;right:0;bottom:0;height:3px;background:var(--yellow)}

/* hero */
.hero{position:absolute;left:0;top:95px;width:1200px;height:567px;background:radial-gradient(ellipse at 60% 40%,#fafafa 0%,#ececec 60%,#e2e2e2 100%)}
.hero-title{position:absolute;left:98px;top:198px;font-weight:800;color:var(--ink);text-transform:uppercase}
.hero-title .l1{display:block;font-size:38px;line-height:42px}
.hero-title .l2{display:block;font-size:27px;line-height:34px}
.btn-dark{position:absolute;left:98px;top:293px;width:137px;height:40px;background:var(--dark);color:var(--white);font-weight:700;font-size:15px;line-height:40px;text-align:center;text-transform:uppercase}
.hero-dots{position:absolute;left:98px;top:360px;display:flex;gap:6px}
.hero-dots span{width:13px;height:13px;border-radius:50%;border:1.5px solid #444}
.hero-dots span.on{border-color:var(--yellow-deep)}
.hero-art{position:absolute;left:516px;top:68px;width:684px;height:405px;border-radius:6px;background:linear-gradient(135deg,#3a3f4a 0%,#6d8aa3 40%,#dfe5ea 75%,#f5f5f5 100%)}

/* services */
.services{position:absolute;left:0;top:593px;width:1200px;height:395px}
.services svg.band{position:absolute;left:0;top:0}
.service{position:absolute;top:85px;width:340px;text-align:center}
.service .icon{width:114px;height:114px;margin:0 auto;border-radius:50%;background:var(--white);border:3px solid #f6e27a;display:flex;align-items:center;justify-content:center}
.service h3{font-family:'Raleway',Arial,sans-serif;font-weight:500;font-size:20px;margin-top:30px;color:var(--ink)}
.service p{font-size:11.5px;line-height:21px;color:#4a4a3a;margin:10px auto 0;width:300px}
.service .more{display:inline-block;margin-top:16px;font-size:13px;color:var(--ink)}
.col-rule{position:absolute;top:85px;width:1px;height:270px;background:rgba(0,0,0,.08)}

/* about */
.about{position:absolute;left:0;top:988px;width:1200px;height:468px;background:linear-gradient(160deg,#fbfbfb,#f2f2f2 50%,#fafafa)}
.about-art{position:absolute;left:155px;top:52px;width:318px;height:366px;border-radius:8px;background:linear-gradient(160deg,#d9412f 0%,#f0a21b 35%,#2f8fd6 60%,#6cc04a 80%,#48545f 100%)}
.about h2{position:absolute;left:547px;top:82px;font-family:'Raleway',Arial,sans-serif;font-weight:500;font-size:34px;color:var(--navy)}
.about .brand{position:absolute;left:547px;top:126px;font-size:28px;line-height:30px}
.about p{position:absolute;left:547px;top:176px;width:500px;font-size:11.5px;line-height:20.5px;color:var(--muted)}
.features{position:absolute;left:547px;top:294px;width:560px;display:grid;grid-template-columns:253px 260px;row-gap:8px;list-style:none}
.features li{font-size:11.5px;color:var(--muted);display:flex;align-items:center;gap:11px;line-height:17px}

/* testimonial */
.testimonial{position:absolute;left:0;top:1456px;width:1200px;height:263px;background:linear-gradient(180deg,#262626,#1a1a1a)}
.avatar-ring{position:absolute;left:136px;top:55px;width:142px;height:142px;border-radius:50%;background:var(--yellow)}
.avatar{position:absolute;left:148px;top:58px;width:132px;height:132px;border-radius:50%;background:linear-gradient(180deg,#c9d3dd,#4a5563);border:4px solid var(--white)}
.testimonial h4{position:absolute;left:299px;top:56px;color:var(--yellow);font-size:21px;font-weight:700}
.testimonial blockquote{position:absolute;left:299px;top:100px;width:780px;color:var(--white);font-style:italic;font-size:12.5px;line-height:25px}
.testimonial .cite{position:absolute;left:299px;top:178px;font-size:14px;color:var(--yellow);font-weight:700}
.testimonial .cite span{font-weight:400}

/* blog */
.blog{position:absolute;left:0;top:1719px;width:1200px;height:519px}
.blog h2{position:absolute;left:0;width:1200px;top:44px;text-align:center;font-family:'Raleway',Arial,sans-serif;font-weight:500;font-size:26px;color:var(--ink)}
.blog .divider{position:absolute;left:560px;top:90px}
.post{position:absolute;top:132px;width:310px}
.post .thumb{position:relative;width:310px;height:189px}
.post .date{position:absolute;left:0;bottom:0;width:52px;height:63px;background:rgba(40,40,40,.85);color:var(--white);text-align:center}
.post .date b{display:block;font-size:20px;padding-top:10px;line-height:22px}
.post .date small{font-size:10px;font-weight:600}
.post h3{font-family:'Raleway',Arial,sans-serif;font-weight:500;font-size:18px;margin-top:16px;color:var(--ink)}
.post p{font-size:11.5px;line-height:24px;color:var(--muted);margin-top:4px}
.post .more{display:inline-flex;align-items:center;gap:7px;margin-top:14px;font-size:12.5px;text-transform:uppercase;color:var(--ink)}

/* footer */
.site-footer{position:absolute;left:0;top:2238px;width:1200px;height:280px;background:var(--footer);color:var(--white)}
.site-footer .brand{position:absolute;left:98px;top:53px;font-size:28px;line-height:32px}
.contact-line{position:absolute;left:98px;display:flex;gap:16px;font-size:13px;line-height:21px}
.f-rule{position:absolute;left:98px;width:265px;height:1px;background:rgba(255,255,255,.12)}
.f-title{position:absolute;top:45px;font-family:'Raleway',Arial,sans-serif;font-size:19px;font-weight:500}
.quick-links{position:absolute;left:447px;top:86px;list-style:none}
.quick-links li{font-size:12px;line-height:29px;display:flex;align-items:center;gap:13px;text-transform:uppercase}
.newsletter p{position:absolute;left:638px;top:91px;width:240px;font-size:11.5px;line-height:20px}
.newsletter .field{position:absolute;left:638px;top:136px;width:247px;height:39px;background:var(--white);color:#555;font-size:11px;line-height:39px;padding-left:14px}
.newsletter .subscribe{position:absolute;left:638px;top:186px;width:89px;height:36px;background:var(--yellow);color:var(--ink);font-size:11px;line-height:36px;text-align:center;text-transform:uppercase}
.social{position:absolute;left:966px;top:88px;list-style:none}
.social li{display:flex;align-items:center;gap:12px;font-size:14px;line-height:36px}
.social li i{width:24px;height:24px;border-radius:50%;border:1.5px solid #ddd;display:block}
.copyright{position:absolute;left:0;top:2518px;width:1200px;height:61px;background:var(--darker);color:var(--white);font-size:13px;line-height:61px;text-align:center}
</style>
</head>
<body>

<header class="site-header">
  <div class="brand">Overthread</div>
  <nav class="main-nav">
    <a class="active">Home</a><a>Our Services</a><a>About Us</a><a>Our Clients</a><a>Contact Us</a>
  </nav>
</header>

<section class="hero">
  <h1 class="hero-title"><span class="l1">Specialised</span><span class="l2">Software Development</span></h1>
  <div class="btn-dark">Read More</div>
  <div class="hero-dots"><span class="on"></span><span></span><span></span></div>
  <div class="hero-art" role="img" aria-label="Fanned row of desktop monitors and a tablet showing website layouts"></div>
</section>

<section class="services">
  <svg class="band" width="1200" height="395" viewBox="0 0 1200 395"><polygon points="0,69 600,0 1200,69 1200,395 0,395" fill="#fcd518"/></svg>
  <div class="col-rule" style="left:427px"></div>
  <div class="col-rule" style="left:778px"></div>

  <div class="service" style="left:79px">
    <div class="icon"><svg width="48" height="48" viewBox="0 0 48 48"><path d="M6 14h11a5 5 0 1 1 8 0h11v11a5 5 0 1 0 0 8v11H25a5 5 0 1 0-8 0H6z" fill="#2b2b2b"/></svg></div>
    <h3>Software Developer</h3>
    <p>Sed ut perspiciatis unde omnis iste natus error sit voluptatem accusantium doloremque laudantium, totam rem aperiam, eaque ipsa quae</p>
    <span class="more">Read More <svg width="10" height="10" viewBox="0 0 10 10"><circle cx="5" cy="5" r="5" fill="#222"/><path d="M4 2.8 6.2 5 4 7.2" stroke="#fcd518" stroke-width="1.4" fill="none"/></svg></span>
  </div>
  <div class="service" style="left:430px">
    <div class="icon"><svg width="52" height="48" viewBox="0 0 52 48"><rect x="3" y="5" width="46" height="30" rx="2" fill="none" stroke="#2b2b2b" stroke-width="5"/><rect x="22" y="35" width="8" height="7" fill="#2b2b2b"/><rect x="14" y="41" width="24" height="4" fill="#2b2b2b"/></svg></div>
    <h3>Web Applications</h3>
    <p>Sed ut perspiciatis unde omnis iste natus error sit voluptatem accusantium doloremque laudantium, totam rem aperiam, eaque ipsa quae</p>
    <span class="more">Read More <svg width="10" height="10" viewBox="0 0 10 10"><circle cx="5" cy="5" r="5" fill="#222"/><path d="M4 2.8 6.2 5 4 7.2" stroke="#fcd518" stroke-width="1.4" fill="none"/></svg></span>
  </div>
  <div class="service" style="left:774px">
    <div class="icon"><svg width="30" height="50" viewBox="0 0 30 50"><rect x="2" y="2" width="26" height="46" rx="4" fill="none" stroke="#2b2b2b" stroke-width="3.5"/><rect x="6" y="8" width="18" height="30" fill="#2b2b2b"/><circle cx="15" cy="43" r="2" fill="#2b2b2b"/></svg></div>
    <h3>Mobile Apps</h3>
    <p>Sed ut perspiciatis unde omnis iste natus error sit voluptatem accusantium doloremque laudantium, totam rem aperiam, eaque ipsa quae</p>
    <span class="more">Read More <svg width="10" height="10" viewBox="0 0 10 10"><circle cx="5" cy="5" r="5" fill="#222"/><path d="M4 2.8 6.2 5 4 7.2" stroke="#fcd518" stroke-width="1.4" fill="none"/></svg></span>
  </div>
</section>

<section class="about">
  <div class="about-art" role="img" aria-label="Isometric smartphone with stacked colourful app interface layers"></div>
  <h2>ABOUT OUR COMPANY</h2>
  <div class="brand">Overthread</div>
  <p>Sed ut perspiciatis unde omnis iste natus error sit voluptatem accusantium doloremque laudantium, totam rem aperiam, eaque ipsa quae ab illo inventore veritatis et quasi architecto beatae vitae dicta sunt explicabo. Nemo enim ipsam voluptatem quia voluptas sit aspernatur aut odit aut fugit, sed quia consequuntur magni dolores eos qui ratione voluptatem sequi nesciunt. Neque porro quisquam est, qui dolorem ipsum quia dolor sit amet.</p>
  <ul class="features">
    <li><svg width="10" height="10" viewBox="0 0 10 10"><circle cx="5" cy="5" r="5" fill="#222"/><path d="M4 2.8 6.2 5 4 7.2" stroke="#fff" stroke-width="1.4" fill="none"/></svg>Specialized software development</li>
    <li><svg width="10" height="10" viewBox="0 0 10 10"><circle cx="5" cy="5" r="5" fill="#222"/><path d="M4 2.8 6.2 5 4 7.2" stroke="#fff" stroke-width="1.4" fill="none"/></svg>Cutting edge software custom designed</li>
    <li><svg width="10" height="10" viewBox="0 0 10 10"><circle cx="5" cy="5" r="5" fill="#222"/><path d="M4 2.8 6.2 5 4 7.2" stroke="#fff" stroke-width="1.4" fill="none"/></svg>Custom software and consulting</li>
    <li><svg width="10" height="10" viewBox="0 0 10 10"><circle cx="5" cy="5" r="5" fill="#222"/><path d="M4 2.8 6.2 5 4 7.2" stroke="#fff" stroke-width="1.4" fill="none"/></svg>High end web and mobile applications</li>
    <li><svg width="10" height="10" viewBox="0 0 10 10"><circle cx="5" cy="5" r="5" fill="#222"/><path d="M4 2.8 6.2 5 4 7.2" stroke="#fff" stroke-width="1.4" fill="none"/></svg>Modern, user friendly software</li>
  </ul>
</section>

<section class="testimonial" role="img" aria-label="Dark city skyline backdrop">
  <div class="avatar-ring"></div>
  <div class="avatar" role="img" aria-label="Client portrait"></div>
  <h4>TESTIMONIALS</h4>
  <blockquote>“ &nbsp;Lorem ipsum dolor sit amet, consectetur adipiscing elit, sed do eiusmod tempor incididunt ut labore et dolore magna aliqua. Ut enim ad minim veniam, quis nostrud exercitation ullamco laboris nisi ut aliquip ex ea commodo consequat. Duis aute irure dolor in reprehenderit in voluptate velit esse cillum dolore eu fugiat nulla pariatur. Excepteur sint occaecat</blockquote>
  <div class="cite">Jon Daley <span>- Overthread</span></div>
</section>

<section class="blog">
  <h2>LATEST BLOG</h2>
  <svg class="divider" width="80" height="14" viewBox="0 0 80 14"><line x1="0" y1="7" x2="80" y2="7" stroke="#f2c500" stroke-width="1.5"/><circle cx="10" cy="7" r="5" fill="#fff" stroke="#f2c500" stroke-width="1.5"/><circle cx="40" cy="7" r="5" fill="#fff" stroke="#f2c500" stroke-width="1.5"/><circle cx="70" cy="7" r="5" fill="#fff" stroke="#f2c500" stroke-width="1.5"/></svg>

  <article class="post" style="left:98px">
    <div class="thumb" role="img" aria-label="Hands using a tablet on a wooden table beside a plant" style="background:linear-gradient(135deg,#7a4a33,#c9a58a 55%,#e9e2da)"><div class="date"><b>02</b><small>JUN</small></div></div>
    <h3>Lorem ipsum dolor sit amet,</h3>
    <p>Lorem ipsum dolor sit amet, consectetur adipiscing elit. Sed blandit massa vel mauris sollicitudin dignissim. Lorem ipsum dolor sit amet, consectetur</p>
    <span class="more">Read More <svg width="10" height="10" viewBox="0 0 10 10"><circle cx="5" cy="5" r="5" fill="#222"/><path d="M4 2.8 6.2 5 4 7.2" stroke="#fff" stroke-width="1.4" fill="none"/></svg></span>
  </article>
  <article class="post" style="left:444px">
    <div class="thumb" role="img" aria-label="Person working on a laptop holding a phone" style="background:linear-gradient(135deg,#3a3430,#a9958a 50%,#d9693a)"><div class="date"><b>02</b><small>JUN</small></div></div>
    <h3>Lorem ipsum dolor sit amet,</h3>
    <p>Lorem ipsum dolor sit amet, consectetur adipiscing elit. Sed blandit massa vel mauris sollicitudin dignissim. Lorem ipsum dolor sit amet, consectetur</p>
    <span class="more">Read More <svg width="10" height="10" viewBox="0 0 10 10"><circle cx="5" cy="5" r="5" fill="#222"/><path d="M4 2.8 6.2 5 4 7.2" stroke="#fff" stroke-width="1.4" fill="none"/></svg></span>
  </article>
  <article class="post" style="left:790px">
    <div class="thumb" role="img" aria-label="Laptop on a desk with web design sketches and coloured pencils" style="background:linear-gradient(135deg,#5d4a36,#b89a6a 45%,#e8c23a 65%,#3c3c3c)"><div class="date"><b>02</b><small>JUN</small></div></div>
    <h3>Lorem ipsum dolor sit amet,</h3>
    <p>Lorem ipsum dolor sit amet, consectetur adipiscing elit. Sed blandit massa vel mauris sollicitudin dignissim. Lorem ipsum dolor sit amet, consectetur</p>
    <span class="more">Read More <svg width="10" height="10" viewBox="0 0 10 10"><circle cx="5" cy="5" r="5" fill="#222"/><path d="M4 2.8 6.2 5 4 7.2" stroke="#fff" stroke-width="1.4" fill="none"/></svg></span>
  </article>
</section>

<footer class="site-footer">
  <div class="brand">Overthread</div>
  <div class="contact-line" style="top:109px"><svg width="12" height="16" viewBox="0 0 12 16"><path d="M6 0a6 6 0 0 0-6 6c0 4.5 6 10 6 10s6-5.5 6-10a6 6 0 0 0-6-6zm0 8.3A2.3 2.3 0 1 1 6 3.7a2.3 2.3 0 0 1 0 4.6z" fill="#fff"/></svg><span>118 Larkmoor Ave, #2368<br>Fenwick, California 90412 USA</span></div>
  <div class="f-rule" style="top:160px"></div>
  <div class="contact-line" style="top:169px"><svg width="14" height="14" viewBox="0 0 14 14"><path d="M3 0l3 3-2 2a9 9 0 0 0 5 5l2-2 3 3-2 3C6 14 0 8 0 2z" fill="#fff"/></svg><span>Call Us +(401) 555 - 0172</span></div>
  <div class="f-rule" style="top:200px"></div>
  <div class="contact-line" style="top:209px"><svg width="15" height="12" viewBox="0 0 15 12"><rect x=".75" y=".75" width="13.5" height="10.5" fill="none" stroke="#fff" stroke-width="1.5"/><path d="M1 1l6.5 5.5L14 1" fill="none" stroke="#fff" stroke-width="1.5"/></svg><span>info@overthread.example</span></div>

  <div class="f-title" style="left:447px">QUICK LINKS</div>
  <ul class="quick-links">
    <li><svg width="5" height="8" viewBox="0 0 5 8"><path d="M0 0l5 4-5 4z" fill="#fff"/></svg>Solutions</li>
    <li><svg width="5" height="8" viewBox="0 0 5 8"><path d="M0 0l5 4-5 4z" fill="#fff"/></svg>Services</li>
    <li><svg width="5" height="8" viewBox="0 0 5 8"><path d="M0 0l5 4-5 4z" fill="#fff"/></svg>About Us</li>
    <li><svg width="5" height="8" viewBox="0 0 5 8"><path d="M0 0l5 4-5 4z" fill="#fff"/></svg>Support</li>
    <li><svg width="5" height="8" viewBox="0 0 5 8"><path d="M0 0l5 4-5 4z" fill="#fff"/></svg>FAQs</li>
  </ul>

  <div class="newsletter">
    <div class="f-title" style="left:638px">JOIN OUR NEWSLETTER</div>
    <p>Excepteur sint occaecat cupidatat non proident, sunt in culpa qui</p>
    <div class="field">Enter Name</div>
    <div class="subscribe">Subscribe</div>
  </div>

  <div class="f-title" style="left:966px">SOCIAL MEDIA</div>
  <ul class="social">
    <li><i></i>Facepage</li>
    <li><i></i>Chirper</li>
    <li><i></i>Globeplus</li>
    <li><i></i>Viewtube</li>
  </ul>
</footer>

<div class="copyright">© 2016 Overthread.. All Rights Reserved.</div>

</body>
</html>
```